Business Card Design Harbourline Flooring

We are a Mobile Flooring Company servicing the Central Coast NSW and Newcastle.We sell and Install Bamboo flooring, laminate flooring and engineered flooring to do it yourself renovators, builders and home improvement clientsOur prices are very competitive and we have a great colour range and selection.We would like the front of the card to have the wood floorboard image (perhaps as the background) and then have our logo over the top (large) with the logo in spot gloss and all the writing in spot gloss. Details of what we do can be included on the back with the deer image (perhaps in silhouette) in the background. Any other ideas using these images will be appreciated.

Target Market(s)

DIY renovators, builders, home improvement clients

Industry/Entity Type

Flooring

Contact Information for Business Card

Servicing Central Coast to Newcastle
sales@harbourlineflooring.com.au
0438 162 504
www.harbourlineflooring.com.au

Font styles to use
Other font styles liked:
• You decide

Requirements
Must have
• The project must have both files uploaded on the business card the image of the woodland forest/ floorboards in the background - filling the whole business card or half business card with the logo over the top
• The logo and all the writing needs to be spot gloss
Nice to have
• A clear easy to read attractive business card
Should not have
• Too dark

```html
<!DOCTYPE html>
<html lang="en">
<head>
<meta charset="UTF-8">
<title>Harbourline Flooring – Business Card Back</title>
<link href="https://fonts.googleapis.com/css2?family=Open+Sans:ital,wght@0,400;0,600;0,700;1,700&display=swap" rel="stylesheet">
<style>
  :root {
    --card-bg: #ffffff;
    --ink-dark: #111111;
    --ink-brown: #3b1418;
    --deer-tone: #eadfdc;
    --deer-fade: rgba(234, 223, 220, 0);
  }
  * { margin: 0; padding: 0; box-sizing: border-box; }
  html, body {
    width: 1200px;
    height: 741px;
    overflow: hidden;
    background: var(--card-bg);
  }
  .card {
    position: relative;
    width: 1200px;
    height: 741px;
    background: var(--card-bg);
    font-family: "Open Sans", sans-serif;
    overflow: hidden;
  }
  .deer-backdrop {
    position: absolute;
    left: 620px;
    top: 0;
    width: 580px;
    height: 741px;
    background: radial-gradient(ellipse 60% 70% at 45% 50%, var(--deer-tone) 0%, var(--deer-tone) 35%, var(--deer-fade) 100%);
    opacity: 0.8;
  }
  .card-content {
    position: absolute;
    inset: 0;
    text-align: center;
  }
  .service-area {
    position: absolute;
    top: 78px;
    left: 0;
    width: 100%;
    font-size: 31px;
    font-weight: 400;
    letter-spacing: 0.32em;
    color: var(--ink-dark);
    padding-left: 0.32em;
  }
  .business-type {
    position: absolute;
    top: 122px;
    left: 0;
    width: 100%;
    font-size: 28px;
    color: var(--ink-dark);
  }
  .tagline {
    position: absolute;
    top: 164px;
    left: 0;
    width: 100%;
    font-size: 28px;
    font-weight: 700;
    font-style: italic;
    letter-spacing: 0.32em;
    color: var(--ink-brown);
  }
  .products-heading {
    position: absolute;
    top: 250px;
    left: 0;
    width: 100%;
    font-size: 31px;
    font-weight: 700;
    color: var(--ink-brown);
    text-decoration: underline;
    text-underline-offset: 5px;
    text-decoration-thickness: 2px;
  }
  .info-list {
    position: absolute;
    left: 0;
    width: 100%;
    list-style: none;
    font-size: 31px;
    line-height: 43px;
    color: var(--ink-brown);
  }
  .product-list { top: 293px; }
  .audience-list { top: 465px; }
</style>
</head>
<body>
  <div class="card">
    <div class="deer-backdrop" role="img" aria-label="Faint silhouette of a stag standing in profile"></div>
    <div class="card-content">
      <p class="service-area">SERVICING CENTRAL COAST &amp; NEWCASTLE</p>
      <p class="business-type">Mobile flooring retailer</p>
      <p class="tagline">"WE COME TO YOU"</p>
      <p class="products-heading">Products:</p>
      <ul class="info-list product-list">
        <li>Bamboo Flooring</li>
        <li>Engineered Hardwood Flooring</li>
        <li>Laminate Flooring</li>
      </ul>
      <ul class="info-list audience-list">
        <li>DIY renovators</li>
        <li>Builders</li>
        <li>Installation service available</li>
      </ul>
    </div>
  </div>
</body>
</html>
```